Innovative Strategic IT Solutions and Management Consulting

Looking for a fresh design idea to represent a company which specializes in innovative strategic IT solutions focusing on information assurance, enterprise content management, health information technology, web applications, strategic IT solutions and solutions architect.

KELTO...the company name means "new beginning" in Greek or the acronym for Keep-Every-Layer-Tightly-Organized. We pride ourselves in understanding the client's business and needs before proposing an innovative solutions.

Innovation / Secure / Strategy - the core motto

Color: Maroon / Burgundy / Silver / White / Grey / Black

Primary focus color: Burgundy / Silver

```html
<!DOCTYPE html>
<html lang="en">
<head>
<meta charset="utf-8">
<title>KELTO Solutions</title>
<link href="https://fonts.googleapis.com/css2?family=Open+Sans:wght@300;400;600&display=swap" rel="stylesheet">
<style>
:root{
  --burgundy:#5a0f17;
  --maroon:#8c0c0c;
  --button:#7a0a0a;
  --footer:#4a1109;
  --ink:#333;
  --muted:#555;
  --panel:#f0eeee;
  --white:#fff;
  --accent:#e35a4f;
}
*{box-sizing:border-box;margin:0;padding:0}
html,body{width:863px;height:1200px;overflow:hidden;background:var(--white)}
body{font-family:"Open Sans",Arial,sans-serif;color:var(--ink);position:relative}
.site-header{position:absolute;top:0;left:0;width:863px;height:75px;background:var(--white)}
.brand{position:absolute;left:52px;top:18px;display:flex;align-items:center;gap:7px;font-size:30px;font-weight:600;color:var(--maroon);letter-spacing:1px}
.brand-dot{width:12px;height:12px;border-radius:50%;background:var(--maroon)}
.main-nav{position:absolute;top:30px;left:0;width:863px;font-size:10px;color:var(--ink)}
.main-nav a{position:absolute;text-decoration:none;color:inherit;letter-spacing:.3px}
.main-nav a.active::before{content:"";position:absolute;left:0;right:0;top:-6px;height:2px;background:var(--accent)}
.hero{position:absolute;top:75px;left:0;width:863px;height:397px;
  background:linear-gradient(90deg,#4a4d52 0%,#8b8d8f 30%,#9a9895 55%,#7a746e 80%,#5f5955 100%)}
.hero-content{position:absolute;top:95px;left:0;width:863px;text-align:center;color:var(--white)}
.hero-title{font-weight:300;font-size:29px;letter-spacing:.5px}
.hero-sub{font-size:15.5px;margin-top:12px}
.hero-text{font-size:11.5px;font-weight:300;line-height:16px;width:330px;margin:14px auto 0}
.hero-btn{display:inline-block;margin-top:16px;border:2px solid var(--white);padding:9px 12px;font-size:12px;color:var(--white);text-decoration:none}
.hero-arrow{position:absolute;top:178px}
.service-bar{position:absolute;top:472px;left:0;width:863px;height:59px;background:var(--burgundy);color:var(--white);font-size:12.5px}
.service-bar span{position:absolute;top:20px;display:flex;align-items:center;gap:9px}
.about{position:absolute;top:575px;left:0;width:863px;text-align:center}
.about h1{font-size:24px;font-weight:400;color:var(--maroon)}
.about h2{font-size:17.5px;font-weight:400;color:var(--muted);margin-top:16px}
.about p{font-size:11px;line-height:19px;color:var(--ink);margin-top:14px;padding:0 2px}
.features{position:absolute;top:775px;left:0;width:863px;height:265px;background:var(--panel)}
.feature{position:absolute;top:26px;width:220px;text-align:center}
.feature-icon{display:block;margin:0 auto}
.feature h3{font-size:14.5px;font-weight:400;color:var(--maroon);margin-top:8px}
.feature p{font-size:8.5px;line-height:12.5px;color:var(--muted);margin:6px auto 0;width:190px}
.btn{position:absolute;top:208px;width:95px;height:31px;background:var(--button);color:var(--white);font-size:12px;text-align:center;line-height:31px;text-decoration:none;box-shadow:2px 2px 3px rgba(0,0,0,.35)}
.site-footer{position:absolute;top:1044px;left:0;width:863px;height:156px;background:var(--footer);color:var(--white)}
.footer-col{position:absolute;top:30px}
.footer-col h4{font-size:18px;font-weight:300;margin-bottom:10px}
.footer-col li{list-style:none;font-size:11px;line-height:21px}
.socials{display:flex;gap:10px;margin-top:4px}
.socials span{width:21px;height:21px;border:1.5px solid var(--white);border-radius:50%}
</style>
</head>
<body>
<header class="site-header">
  <div class="brand"><span>KELTO</span><span class="brand-dot"></span></div>
  <nav class="main-nav">
    <a class="active" href="#" style="left:441px">HOME</a>
    <a href="#" style="left:504px">SOLUTIONS</a>
    <a href="#" style="left:589px">STRATEGY</a>
    <a href="#" style="left:668px">SECURITY</a>
    <a href="#" style="left:744px">TECHNOLOGIES</a>
  </nav>
</header>

<section class="hero" role="img" aria-label="Blurred photo of business people meeting around a conference table">
  <svg class="hero-arrow" style="left:50px" width="14" height="40" viewBox="0 0 14 40"><polyline points="11,3 3,20 11,37" fill="none" stroke="#fff" stroke-width="3"/></svg>
  <svg class="hero-arrow" style="left:799px" width="14" height="40" viewBox="0 0 14 40"><polyline points="3,3 11,20 3,37" fill="none" stroke="#fff" stroke-width="3"/></svg>
  <div class="hero-content">
    <div class="hero-title">INNOVATIVE STRATEGIC IT SOLUTIONS</div>
    <div class="hero-sub">Build/develop Custum website and Web Application</div>
    <p class="hero-text">Web Development offers professional Website development services to help you successfully plan, create, maintain and market your Web development project.</p>
    <a class="hero-btn" href="#">LEARN MORE</a>
  </div>
</section>

<nav class="service-bar">
  <span style="left:52px"><svg width="14" height="14" viewBox="0 0 14 14"><rect x="1" y="3" width="10" height="10" fill="none" stroke="#fff" stroke-width="1.5"/><path d="M5 9l8-8" stroke="#fff" stroke-width="2"/></svg>Solutions Architect</span>
  <span style="left:255px"><svg width="13" height="14" viewBox="0 0 13 14"><rect x="1" y="2" width="11" height="11" fill="none" stroke="#fff" stroke-width="1.5"/><rect x="1" y="2" width="11" height="3" fill="#fff"/><rect x="4" y="7" width="2" height="2" fill="#fff"/><rect x="7" y="7" width="2" height="2" fill="#fff"/></svg>Strategic Management</span>
  <span style="left:491px"><svg width="14" height="14" viewBox="0 0 14 14"><path d="M2 1h6l3 3v4" fill="none" stroke="#fff" stroke-width="1.5"/><path d="M2 1v12h5" fill="none" stroke="#fff" stroke-width="1.5"/><circle cx="10.5" cy="10.5" r="2.5" fill="#fff"/></svg>Application Development</span>
  <span style="left:727px"><svg width="12" height="14" viewBox="0 0 12 14"><rect x="1" y="1" width="10" height="12" fill="none" stroke="#fff" stroke-width="1.5"/><path d="M6 4v6M3 7h6" stroke="#fff" stroke-width="2"/></svg>Health IT</span>
</nav>

<section class="about">
  <h1>ABOUT KELTO SOLUTIONS</h1>
  <h2>I can help construct an IT solution.</h2>
  <p>Our team of talented designers and developers has been providing custom design and application development to clients around the world.Brightline Works is a global providerof<br>innovative solutions and capabilities to clients worldwide, with offerings web development services, application services, systems integration, custom software devel opment,<br>maintenance, independent testing and validation services, Web Marketing, Search Engine Optimization and also deals with computerperipherals</p>
</section>

<section class="features">
  <div class="feature" style="left:54px">
    <svg class="feature-icon" width="76" height="76" viewBox="0 0 76 76"><circle cx="38" cy="38" r="35" fill="#fff" stroke="#111" stroke-width="3.5"/><rect x="19" y="24" width="38" height="26" rx="2" fill="none" stroke="#111" stroke-width="3"/><path d="M30 56h16M38 50v6" stroke="#111" stroke-width="3"/><path d="M28 44l16-14" stroke="#111" stroke-width="2.5"/></svg>
    <h3>Innovative Solutions</h3>
    <p>We create meaningful websites that offersimplistic user experiences, achieve highr ankings on the mo st popular search engines and promote your bran dto the widest possible audience.</p>
  </div>
  <div class="feature" style="left:317px">
    <svg class="feature-icon" width="76" height="76" viewBox="0 0 76 76"><circle cx="38" cy="38" r="35" fill="#fff" stroke="#111" stroke-width="3.5"/><rect x="29" y="16" width="18" height="6" fill="#111"/><rect x="25" y="24" width="26" height="34" rx="3" fill="#111"/><rect x="29" y="31" width="18" height="18" fill="#fff"/><path d="M38 34v12M32 40h12" stroke="#111" stroke-width="4"/></svg>
    <h3>Health IT</h3>
    <p>Our emphasis on quality code and our straight-forward approach to custom web solutions will streamline your operations. We focus on scalable development to ensur e pain-free maintenance and application longevity.</p>
  </div>
  <div class="feature" style="left:594px">
    <svg class="feature-icon" width="76" height="76" viewBox="0 0 76 76"><circle cx="38" cy="38" r="35" fill="#fff" stroke="#111" stroke-width="3.5"/><rect x="21" y="44" width="6" height="12" fill="#111"/><rect x="30" y="38" width="6" height="18" fill="#111"/><rect x="39" y="32" width="6" height="24" fill="#111"/><rect x="48" y="26" width="6" height="30" fill="#111"/><path d="M20 38L46 18" stroke="#111" stroke-width="3"/><polygon points="50,14 40,16 47,23" fill="#111"/></svg>
    <h3>Information Assurance</h3>
    <p>Our Internet marketing and content expertswork closely with clients to maximize their online prese- nce. Obtain top rankings for desired search terms and drive qualified leads that are crucial to buil ding your business and brand.</p>
  </div>
  <a class="btn" href="#" style="left:116px">Read More</a>
  <a class="btn" href="#" style="left:380px">Read More</a>
  <a class="btn" href="#" style="left:656px">Read More</a>
</section>

<footer class="site-footer">
  <div class="footer-col" style="left:51px"><h4>Services</h4><ul><li>Solutions Architect</li><li>Strategic Management</li><li>Application Development</li><li>Health IT</li></ul></div>
  <div class="footer-col" style="left:210px"><h4>About Us</h4><ul><li>Company Profile</li><li>Our Team</li><li>Company Culture</li></ul></div>
  <div class="footer-col" style="left:374px"><h4>Stay Connected</h4><div class="socials"><span></span><span></span><span></span><span></span></div></div>
  <div class="footer-col" style="left:596px"><h4>Blog</h4><ul><li>Construct An</li><li>IT Solution.</li></ul></div>
  <div class="footer-col" style="left:730px"><h4>Legal Stuff</h4><ul style="line-height:15px"><li style="line-height:15px">© 2014 KELTO</li><li style="line-height:15px">IT solutions . All</li><li style="line-height:15px">Rights Reserved</li></ul></div>
</footer>
</body>
</html>
```